Bref créative
Brightfield pest control
Stationary business card project for brightfield pest control
Professional
Doug Harlan
4120 w pinecrest ln. meridian idaho 83619
dharlan77@mailvista.net
ALL SERVICES GUARANTEED
Residential.Commercial Service.Certified specialist.Free Estimates
This is the company logo.

```html
<!DOCTYPE html>
<html lang="en">
<head>
<meta charset="utf-8">
<title>Brightfield pest control – business card</title>
<link href="https://fonts.googleapis.com/css2?family=Arimo:wght@400;700&display=swap" rel="stylesheet">
<style>
  :root {
    --bg: #ededed;
    --card: #ffffff;
    --green: #3cad4b;
    --orange: #f47c20;
    --ink: #1a1a1a;
    --rule: #555555;
  }
  * { margin: 0; padding: 0; box-sizing: border-box; }
  html, body { width: 1200px; height: 511px; overflow: hidden; background: var(--bg); }
  body { position: relative; font-family: "Arimo", Arial, sans-serif; color: var(--ink); }

  .card {
    position: absolute;
    top: 72px;
    width: 534px;
    height: 367px;
    border-radius: 24px;
    overflow: hidden;
    box-shadow: 0 4px 12px rgba(0,0,0,0.22);
  }
  .card-front { left: 36px; background: var(--card); }
  .card-back { left: 635px; background: var(--green); color: #fff; }

  .front-band { position: absolute; left: 0; bottom: 0; width: 100%; height: 34px; }

  .brand-block {
    position: absolute; left: 10px; top: 96px; width: 250px; text-align: center;
  }
  .brand-name {
    font-weight: 700; color: var(--orange); font-size: 34px; line-height: 1.05;
  }
  .tagline { margin-top: 18px; font-size: 11.5px; line-height: 1.35; }

  .divider {
    position: absolute; left: 257px; top: 60px; width: 2px; height: 168px; background: var(--rule);
  }
  .holder-name {
    position: absolute; left: 352px; top: 64px; font-size: 23px; color: var(--orange);
  }
  .contact {
    position: absolute; left: 286px; top: 170px; font-size: 15px; line-height: 1.55; list-style: none;
  }

  .back-brand {
    position: absolute; left: 0; top: 78px; width: 100%; text-align: center;
    font-weight: 700; font-size: 50px; line-height: 1.05;
  }
  .back-tagline {
    position: absolute; left: 0; top: 292px; width: 100%; text-align: center;
    font-size: 13px; line-height: 1.45;
  }
</style>
</head>
<body>
  <section class="card card-front">
    <div class="brand-block">
      <div class="brand-name">brightfield<br>pest control</div>
      <p class="tagline">ALL SERVICES GUARANTEED<br>Residential.Commercial Service.<br>Certified specialist.Free Estimates</p>
    </div>
    <div class="divider"></div>
    <h1 class="holder-name">Doug Harlan</h1>
    <ul class="contact">
      <li>Address : 4120 w pinecrest ln.</li>
      <li>meridian idaho 83619</li>
      <li>Cell : (208)555-0142</li>
      <li>Email : dharlan77@mailvista.net</li>
    </ul>
    <svg class="front-band" viewBox="0 0 534 34" preserveAspectRatio="none">
      <rect x="0" y="12" width="534" height="22" fill="var(--green)"/>
      <polygon points="440,34 470,0 534,0 534,34" fill="var(--orange)"/>
    </svg>
  </section>

  <section class="card card-back">
    <div class="back-brand">brightfield<br>pest control</div>
    <p class="back-tagline">ALL SERVICES GUARANTEED<br>Residential.Commercial Service.Certified specialist.Free Estimates</p>
  </section>
</body>
</html>
```